Website Redesign for Allies of Beit Norah

Beit Norah's mission is to enable chronically ill, disabled, infirm, and terminally ill people in Israel to live with dignity. Allies of Beit Norah raises awareness of and funds for Beit Norah to its friends in the USA. This project is to redesign Allies of Beit Norah's current site (https://alliesofbeitnorah.example/).

The redesigned site will use current colors, logo, and text, but will get new images. The design must 1) project a friendlier vibe, 2) be emotionally engaging and inviting (so people will make donations), and 3) be clear (so people get an understanding of Beit Norah at a glance).

Please provide a homepage design and one inner page design.
Please provide PSD files so we can see all layers of the design.
Please take the colors from the current logo.

Target Market(s)

high net worth individuals who are interested in Israel, Jewish causes, philanthropic elder care and medical care.

Industry/Entity Type

non-profit fundraising organization for old and young in Israel who are chronically ill, disabled, infirm, and terminally ill.

Number of Pages Required

2 page

Font styles to use
Sans Serif

Colors
0054AA
0677BA
7BADD7
CADEEF
E8F1F8
EB3D1F
EC4F4E
F09395
F8D3D4
FCEDEE

Requirements
Must have
• PSD files. site colors from logo (red and blue). friendly, emotionally engaging and clear so people will donate.
Should not have
• not too flashy - target market is older

```html
<!DOCTYPE html>
<html lang="en">
<head>
<meta charset="utf-8">
<title>Allies of Beit Norah</title>
<link href="https://fonts.googleapis.com/css2?family=Roboto:wght@400;500;700&family=Montserrat:wght@500;600&display=swap" rel="stylesheet">
<style>
:root{
  --navy:#1e3d9b;
  --blue:#0054aa;
  --red:#e2282b;
  --red-soft:#ec4f4e;
  --pink:#f8d3d4;
  --ink:#222;
  --grey:#555;
  --light:#f4f5f8;
  --footer:#2a2a2a;
  --btn:linear-gradient(90deg,#1e3d9b 0%,#e2282b 100%);
}
*{box-sizing:border-box;margin:0;padding:0}
html,body{width:1200px;height:3569px;overflow:hidden}
body{position:relative;font-family:"Roboto",sans-serif;color:var(--ink);background:#fff}
.abs{position:absolute}
.btn{position:absolute;display:flex;align-items:center;justify-content:center;color:#fff;font-weight:700;font-size:15px;border-radius:5px;background:var(--btn)}
.brand{left:111px;top:24px;display:flex;align-items:center;gap:12px}
.brand-mark{width:52px;height:52px;border-radius:50%;background:var(--red)}
.brand-name{font-weight:700;font-size:24px;line-height:25px;color:var(--navy);width:170px}
.nav{left:403px;top:50px;display:flex;gap:40px;font-size:15px;color:#333}
.donate-top{left:975px;top:40px;width:114px;height:43px}
.hero{left:0;top:119px;width:1200px;height:557px;background:linear-gradient(90deg,#eef0f3 0%,#e3e6ea 45%,#b7c0cc 70%,#8e9aab 100%)}
.hero-title{left:111px;top:258px;font-weight:700;font-size:46px;line-height:64px;color:var(--navy)}
.hero-title .red{color:var(--red)}
.hero-btn{left:112px;top:484px;width:146px;height:41px;font-size:15px}
.arrow{top:378px}
.sec-title{font-family:"Montserrat",sans-serif;font-weight:600;color:#222}
.video{left:111px;top:830px;width:427px;height:302px;border-radius:22px;background:linear-gradient(135deg,#c9c0b6,#8c7d70 60%,#5d5149);overflow:hidden}
.video-caption{left:0;bottom:22px;width:100%;color:#fff;font-size:22px;white-space:nowrap}
.play{left:300px;top:958px}
.slider-line{left:600px;top:871px;width:488px;height:4px;background:var(--navy)}
.amount{top:826px;font-size:15px;color:#333}
.tooltip{left:725px;top:924px;width:349px;height:42px;border-radius:21px;background:#fff;box-shadow:0 2px 10px rgba(0,0,0,.12);font-size:14px;color:#444;display:flex;align-items:center;justify-content:center}
.news{left:0;top:1219px;width:1200px;height:496px;background:linear-gradient(135deg,#2455b8,#1c47a6 60%,#2a5cbd)}
.tab{position:absolute;top:1302px;height:42px;border:2px solid #fff;border-radius:4px;font-weight:700;font-size:15px;display:flex;align-items:center;justify-content:center}
.card{position:absolute;top:1401px;width:476px;height:248px;background:#fff;display:flex}
.card-img{width:212px;height:100%}
.card-body{padding:30px 28px 0 20px;width:264px}
.card-body h3{font-size:17px;font-weight:500;line-height:25px;color:#222}
.card-date{color:var(--red);font-size:12.5px;margin-top:12px}
.card-text{color:#666;font-size:14.5px;line-height:22px;margin-top:12px}
.card-link{color:var(--navy);font-weight:700;font-size:14.5px;margin-top:14px}
.stat{position:absolute;top:1894px;width:170px;text-align:center}
.ring{width:125px;height:125px;border-radius:50%;background:var(--pink);margin:0 auto;display:flex;align-items:center;justify-content:center}
.ring .core{width:105px;height:105px;border-radius:50%;background:var(--navy);display:flex;align-items:center;justify-content:center}
.stat-num{font-size:21px;margin-top:24px;color:#222}
.stat-label{font-size:15px;line-height:22px;color:#444;margin-top:4px}
.profile{left:0;top:2185px;width:1200px;height:444px;background:linear-gradient(90deg,#e7e9ec,#f2f2f2)}
.support{left:0;top:2185px;width:1200px;height:444px;background:linear-gradient(135deg,#e8332c,#e33a30 60%,#d8201f);clip-path:polygon(626px 0,1200px 0,1200px 444px,575px 444px)}
.p-text{font-size:15.5px;line-height:22px}
.white-btn{position:absolute;background:#fff;color:var(--red);font-weight:700;font-size:15px;border-radius:5px;display:flex;align-items:center;justify-content:center}
.frame-red{left:115px;top:2716px;width:257px;height:274px;border-top:2px solid var(--red);border-left:2px solid var(--red)}
.frame-blue{left:260px;top:2830px;width:232px;height:274px;border-bottom:2px solid var(--navy);border-right:2px solid var(--navy)}
.about-img{left:123px;top:2724px;width:362px;height:366px;background:linear-gradient(160deg,#4a3a30,#b89a8a 55%,#d9bdc4)}
.about-text{left:574px;top:2826px;width:474px;font-size:17px;line-height:30px;color:#333;text-align:justify}
.footer{left:0;top:3190px;width:1200px;height:379px;background:var(--footer);color:#fff}
.f-head{font-weight:700;font-size:18px;top:3290px}
.f-links{font-size:15px;line-height:26px;color:#eee}
.social{top:3428px;width:40px;height:40px;border-radius:50%;background:#fff;display:flex;align-items:center;justify-content:center}
.social span{width:14px;height:14px;border-radius:50%;background:var(--red)}
</style>
</head>
<body>

<header>
  <div class="abs brand">
    <div class="brand-mark"></div>
    <div class="brand-name">ALLIES OF<br>BEIT NORAH</div>
  </div>
  <nav class="abs nav"><span>About Us</span><span>Our Impact</span><span>Newsroom</span><span>Contact Us</span><span>Get Involved</span></nav>
  <div class="btn donate-top">Donate Now</div>
</header>

<section>
  <div class="abs hero" role="img" aria-label="Photo of an elderly woman seated in a wheelchair by a bright window"></div>
  <h1 class="abs hero-title">Help Us Care For The<br><span class="red">Builders Of Startup Nationand</span><br>Return Her Favor Of Service.</h1>
  <div class="btn hero-btn">Make a Donation</div>
  <svg class="abs arrow" style="left:40px" width="26" height="42" viewBox="0 0 26 42"><path d="M22 3 4 21l18 18" fill="none" stroke="var(--navy)" stroke-width="4"/></svg>
  <svg class="abs arrow" style="left:1140px" width="26" height="42" viewBox="0 0 26 42"><path d="M4 3l18 18L4 39" fill="none" stroke="#fff" stroke-width="4"/></svg>
</section>

<section>
  <h2 class="abs sec-title" style="left:111px;top:760px;font-size:25px">How We Care For Israel's Builders</h2>
  <div class="abs video" role="img" aria-label="Video still of an elderly man with a white beard speaking">
    <div class="abs video-caption">wife suffers from vertigo and dizziness.</div>
  </div>
  <svg class="abs play" width="52" height="52" viewBox="0 0 52 52"><circle cx="26" cy="26" r="25" fill="var(--red)"/><path d="M20 15v22l18-11z" fill="#fff"/></svg>

  <h2 class="abs sec-title" style="left:709px;top:757px;font-size:29px">How You Can Help</h2>
  <span class="abs amount" style="left:638px">₹3,000</span>
  <span class="abs amount" style="left:762px">₹5,000</span>
  <span class="abs amount" style="left:886px">₹9,000</span>
  <span class="abs amount" style="left:1004px">₹20,000</span>
  <div class="abs slider-line"></div>
  <svg class="abs" style="left:600px;top:853px" width="488" height="40" viewBox="0 0 488 40">
    <g fill="#fff" stroke="#ddd"><circle cx="61" cy="20" r="9"/><circle cx="185" cy="20" r="9"/><circle cx="432" cy="20" r="9"/></g>
    <g fill="var(--red)"><circle cx="61" cy="20" r="4"/><circle cx="185" cy="20" r="4"/><circle cx="432" cy="20" r="4"/></g>
    <circle cx="308" cy="20" r="17" fill="var(--red)"/><circle cx="308" cy="20" r="5" fill="#fff"/>
  </svg>
  <svg class="abs" style="left:898px;top:914px" width="24" height="12"><path d="M0 12 12 0l12 12z" fill="#fff"/></svg>
  <div class="abs tooltip">Help Purchases an oxygen tank &amp; accessories</div>
  <div class="btn" style="left:788px;top:1009px;width:113px;height:41px">Donation</div>
</section>

<section>
  <div class="abs news"></div>
  <div class="tab" style="left:370px;width:225px;color:#fff">The Impact Of Your Support</div>
  <div class="tab" style="left:606px;width:224px;background:#fff;color:var(--navy)">The Latest At Beit Norah</div>
  <article class="card" style="left:112px">
    <div class="card-img" role="img" aria-label="Photo of an older woman resting in a hospital bed" style="background:linear-gradient(160deg,#cfd8dc,#8fb3c4 60%,#7fa26a)"></div>
    <div class="card-body">
      <h3>Inside Beit Norah - Fall 2022 Newsletter Is Here</h3>
      <div class="card-date">22 DECEMBER 2022</div>
      <p class="card-text">We are proud to bring you another edition of "INSIDE Beit Norah." We all know that the</p>
      <div class="card-link">Read More</div>
    </div>
  </article>
  <article class="card" style="left:612px">
    <div class="card-img" role="img" aria-label="Photo of a young girl visiting her grandfather in a hospital bed" style="background:linear-gradient(160deg,#e6ecef,#b7c8d4 60%,#8ea5b8)"></div>
    <div class="card-body">
      <h3>Beit Norah Assists Tourists of all Abilities</h3>
      <div class="card-date">04 JULY 2022</div>
      <p class="card-text">"Maybe I can do this." Helen Marbury was excited to receive an invitation to her</p>
      <div class="card-link">Read More</div>
    </div>
  </article>
</section>

<section>
  <h2 class="abs" style="left:0;width:1200px;top:1797px;text-align:center;font-size:28px;font-weight:500">Beit Norah’s Services Change Lives</h2>
  <p class="abs" style="left:0;width:1200px;top:1843px;text-align:center;font-size:15px;color:#333">Below are some of Beit Norah's Annual Figures</p>

  <div class="stat" style="left:90px"><div class="ring"><div class="core">
    <svg width="60" height="50" viewBox="0 0 60 50" fill="none" stroke="#fff" stroke-width="2.5"><circle cx="30" cy="14" r="7"/><circle cx="12" cy="18" r="5"/><circle cx="48" cy="18" r="5"/><path d="M18 42c0-9 5-15 12-15s12 6 12 15zM3 40c0-7 4-11 9-11M57 40c0-7-4-11-9-11"/></svg>
  </div></div><div class="stat-num">800,000</div><div class="stat-label">People Helped</div></div>

  <div class="stat" style="left:260px"><div class="ring"><div class="core">
    <svg width="52" height="52" viewBox="0 0 52 52" fill="none" stroke="#fff" stroke-width="2.5"><path d="M8 44V22l6-10 4 4v28M44 44V22l-6-10-4 4v28"/><path d="M26 26l-4-4a3 3 0 0 1 4-4 3 3 0 0 1 4 4z"/></svg>
  </div></div><div class="stat-num">7,000</div><div class="stat-label">Volunteers</div></div>

  <div class="stat" style="left:429px"><div class="ring"><div class="core">
    <svg width="56" height="52" viewBox="0 0 56 52" fill="none" stroke="#fff" stroke-width="2.5"><path d="M6 22v14l12 12h20l12-12V22"/><circle cx="28" cy="18" r="9"/><path d="M22 34h12"/></svg>
  </div></div><div class="stat-num">122</div><div class="stat-label">Branches</div></div>

  <div class="stat" style="left:600px"><div class="ring"><div class="core">
    <svg width="48" height="56" viewBox="0 0 48 56" fill="none" stroke="#fff" stroke-width="2.5"><rect x="6" y="8" width="32" height="42" rx="3"/><rect x="15" y="3" width="14" height="8" rx="2"/><path d="M12 22l3 3 5-5M12 36l3 3 5-5M24 23h8M24 37h4"/><path d="M34 32l9 3v7c0 5-4 8-9 10-5-2-9-5-9-10v-7z"/></svg>
  </div></div><div class="stat-num">509,608</div><div class="stat-label">Medical Equipment<br>Loans</div></div>

  <div class="stat" style="left:769px"><div class="ring"><div class="core">
    <svg width="56" height="52" viewBox="0 0 56 52" fill="none" stroke="#fff" stroke-width="2.5"><path d="M6 4h22v14H14l-6 5V18H6zM30 8h20v12h-3v5l-5-5H32"/><circle cx="16" cy="32" r="5"/><circle cx="40" cy="32" r="5"/><path d="M7 48c0-6 4-9 9-9s9 3 9 9M31 48c0-6 4-9 9-9s9 3 9 9"/></svg>
  </div></div><div class="stat-num">69,909</div><div class="stat-label">Phone Conversations<br>with Homebound</div></div>

  <div class="stat" style="left:939px"><div class="ring"><div class="core">
    <svg width="56" height="56" viewBox="0 0 56 56" fill="none" stroke="#fff" stroke-width="2.5"><path d="M10 14c-4 4-6 12 0 22s18 16 24 14l4-5-7-6-4 3c-5-2-9-6-11-11l3-4-6-7z"/><circle cx="34" cy="22" r="13"/><text x="27" y="26" font-size="10" fill="#fff" stroke="none" font-family="Roboto,sans-serif" font-weight="700">24</text><path d="M44 4v8M40 8h8"/></svg>
  </div></div><div class="stat-num">297,564</div><div class="stat-label">Calls to Emergency<br>Hotline</div></div>
</section>

<section>
  <div class="abs profile" role="img" aria-label="Soft faded photo of a caregiver with an elderly man"></div>
  <div class="abs support"></div>
  <h2 class="abs" style="left:111px;top:2252px;font-size:30px;font-weight:700;color:#222">Our Profile</h2>
  <p class="abs p-text" style="left:111px;top:2322px;width:380px;color:#333">GiveLight Registry revolutionizes philanthropy by providing information that advances transparency so donors can make better decisions.</p>
  <p class="abs p-text" style="left:111px;top:2412px;width:380px;color:#333">Allies of Beit Norah has earned a beit norah registry 2020ninth consecutive 4-star rating from Donor Compass.</p>
  <div class="btn" style="left:111px;top:2512px;width:112px;height:42px">Learn More</div>

  <h2 class="abs" style="left:709px;top:2290px;font-size:30px;font-weight:700;color:#fff">Support Us</h2>
  <p class="abs p-text" style="left:709px;top:2362px;width:390px;color:#fff">Your gift will help provide a vital array of compassionate health and home care services for people of all ages in Israel!</p>
  <div class="white-btn" style="left:709px;top:2467px;width:116px;height:42px">Donate now</div>
</section>

<section>
  <div class="abs frame-red"></div>
  <div class="abs frame-blue"></div>
  <div class="abs about-img" role="img" aria-label="Photo of a distressed older woman sitting on the floor by a window"></div>
  <h2 class="abs" style="left:574px;top:2766px;font-size:25px;font-weight:500;color:#222">About Us</h2>
  <p class="abs about-text">Beit Norah is Israel’s largest volunteer-staffed organization, providing a wide array of compassionate health and home care services for people of all ages, with special programs directed at support for older adults and for children and adults with disabilities.</p>
  <div class="btn" style="left:574px;top:3003px;width:112px;height:42px">Learn More</div>
</section>

<footer>
  <div class="abs footer"></div>
  <div class="abs" style="left:114px;top:3296px;display:flex;align-items:center;gap:12px">
    <div style="width:50px;height:50px;border-radius:50%;background:#fff"></div>
    <div style="color:#fff;font-weight:700;font-size:26px;line-height:26px">ALLIES OF<br>BEIT NORAH</div>
  </div>
  <div class="abs social" style="left:116px"><span></span></div>
  <div class="abs social" style="left:171px"><span></span></div>
  <div class="abs social" style="left:225px"><span></span></div>
  <div class="abs social" style="left:280px"><span></span></div>

  <div class="abs f-head" style="left:407px;color:#fff">QUICK LINKS</div>
  <div class="abs f-links" style="left:407px;top:3330px">About Us<br>Our Impact<br>Newsroom<br>Contact Us<br>Get Involved</div>

  <div class="abs f-head" style="left:581px;color:#fff">CONTACT US</div>
  <svg class="abs" style="left:582px;top:3340px" width="16" height="20" viewBox="0 0 16 20"><path d="M8 0a7 7 0 0 0-7 7c0 5 7 13 7 13s7-8 7-13a7 7 0 0 0-7-7z" fill="#fff"/><circle cx="8" cy="7" r="2.5" fill="var(--footer)"/></svg>
  <div class="abs f-links" style="left:613px;top:3336px">218 Linden Row, Suite 410,<br>Hartwell, NY 10990 USA</div>
  <svg class="abs" style="left:582px;top:3412px" width="18" height="18" viewBox="0 0 18 18"><path d="M3 1l4 4-2 3c1 2 3 4 5 5l3-2 4 4-3 3C8 18 0 10 0 4z" fill="#fff"/></svg>
  <div class="abs f-links" style="left:613px;top:3408px">555.014.2290</div>
  <svg class="abs" style="left:582px;top:3447px" width="18" height="14" viewBox="0 0 18 14"><rect width="18" height="14" rx="1" fill="#fff"/><path d="M1 1l8 7 8-7" fill="none" stroke="var(--footer)" stroke-width="1.5"/></svg>
  <div class="abs f-links" style="left:613px;top:3442px">hello@alliesofbeitnorah.example</div>

  <div class="abs f-head" style="left:867px;color:#fff">NEWSLETTER</div>
  <div class="abs" style="left:867px;top:3339px;width:225px;height:40px;background:#fff;border-radius:4px;font-size:14px;color:#888;display:flex;align-items:center;padding-left:13px">Enter email</div>
  <div class="abs" style="left:1038px;top:3339px;width:54px;height:40px;background:var(--blue);border-radius:0 4px 4px 0;display:flex;align-items:center;justify-content:center">
    <svg width="16" height="12" viewBox="0 0 16 12"><rect width="16" height="12" rx="1" fill="#fff"/><path d="M1 1l7 6 7-6" fill="none" stroke="var(--blue)" stroke-width="1.5"/></svg>
  </div>

  <div class="abs" style="left:0;width:1200px;top:3518px;text-align:center;font-size:15px;color:#eee">©Copyrights 2023 alliesofbeitnorah &nbsp;&nbsp;|&nbsp;&nbsp; All Rights Reserved</div>
</footer>

</body>
</html>
```